Modern 6 page design, business card, and a banner

I need a website design for my CFO service. The service uses proprietary tech, so it needs to be modern. I also need business card and banner design to match the site.
The banner size is 33.75 X 79.25.
I'm open to colors and styles.

Target Market(s)

Startups

Coding

Coded - Design and coding required

Number of Pages Required

5+ page

```html
<!DOCTYPE html>
<html lang="en">
<head>
<meta charset="utf-8">
<title>Tallo — Financial Planning &amp; Mobile Monitoring</title>
<link href="https://fonts.googleapis.com/css2?family=Raleway:wght@300;400;500;600;700&display=swap" rel="stylesheet">
<style>
:root{
  --teal:#14bfae;
  --teal-dark:#0ea597;
  --purple:#7b6cf6;
  --red:#f64447;
  --hero:#1d4b50;
  --ink:#4a4a4a;
  --muted:#6e6e6e;
  --line:#d9d9d9;
  --white:#ffffff;
}
*{box-sizing:border-box;margin:0;padding:0}
html,body{width:1200px;height:4000px;overflow:hidden}
body{font-family:'Raleway',sans-serif;color:var(--ink);background:var(--white);position:relative}
.abs{position:absolute}
.btn{position:absolute;display:flex;align-items:center;justify-content:center;font-size:14px;font-weight:500;letter-spacing:.5px;border-radius:4px;box-shadow:0 4px 10px rgba(0,0,0,.15)}
.btn.notch::after{content:"";position:absolute;top:-7px;left:50%;width:16px;height:14px;margin-left:-8px;border-radius:8px 8px 0 0;background:inherit}

/* hero */
.hero{left:0;top:0;width:1200px;height:640px;background:linear-gradient(180deg,#1e5256 0%,#1a4346 60%,#152e33 100%)}
.nav{top:36px;left:0;width:1200px;height:30px}
.brand{position:absolute;left:153px;top:-4px;font-size:38px;font-weight:300;color:var(--white);letter-spacing:1px}
.nav a{position:absolute;top:0;font-size:14px;color:var(--white);text-decoration:none}
.hero-title{left:155px;top:208px;width:600px;font-size:40px;line-height:46px;font-weight:400;color:var(--white)}
.hero-title b{font-weight:700}
.btn-hero{left:155px;top:377px;width:120px;height:39px;background:var(--white);color:var(--purple)}

/* about */
.about-title{left:155px;top:772px;font-size:50px;font-weight:400;color:var(--purple)}
.about-text{left:155px;top:852px;width:392px;font-size:12.5px;line-height:19.4px;color:var(--muted)}
.about-text p{margin-bottom:19px}
.hl-purple{color:var(--purple)}
.btn-about{left:157px;top:1103px;width:160px;height:38px;background:var(--purple);color:var(--white)}
.exp-card{left:615px;top:880px;width:227px;height:319px;background:rgba(245,247,252,.95);box-shadow:inset 0 0 0 5px #1f2b44}
.exp-num{position:absolute;left:0;width:227px;top:118px;text-align:center;font-size:120px;font-weight:700;line-height:1;color:#5d87b8;letter-spacing:-4px}
.exp-label{position:absolute;left:0;width:227px;top:253px;text-align:center;font-size:14px;color:#333}

/* how it works */
.how-title{left:155px;top:1355px;font-size:50px;font-weight:400;color:var(--white)}
.step{position:absolute;width:230px;text-align:center}
.step .num{position:absolute;font-size:28px;font-weight:300;color:rgba(20,191,174,.4)}
.step h3{font-size:20px;font-weight:500;color:var(--teal);margin-bottom:14px}
.step p{font-size:12.5px;line-height:19px;color:var(--muted)}

/* visual finance */
.vf-title{left:0;width:1200px;top:2212px;text-align:center;font-size:50px;font-weight:400;color:var(--teal)}
.vf-text{left:601px;top:2414px;width:443px;font-size:12.5px;line-height:19px;color:var(--muted)}
.vf-text p{margin-bottom:19px}
.hl-teal{color:var(--teal)}
.btn-vf{left:601px;top:2618px;width:120px;height:39px;background:var(--teal);color:var(--white)}

/* why */
.why-title{left:0;width:1200px;top:2955px;text-align:center;font-size:48px;font-weight:400;color:var(--white)}
.why-text{left:250px;width:700px;top:3032px;text-align:center;font-size:13px;line-height:24px;color:var(--white)}
.why-text p{margin-bottom:6px}
.btn-why{left:534px;top:3204px;width:123px;height:40px;background:var(--white);color:var(--red)}

/* contact */
.contact-title{left:0;width:1200px;top:3412px;text-align:center;font-size:50px;font-weight:400;color:var(--red)}
.field{position:absolute;left:155px;width:586px;border:1px solid var(--line);border-radius:3px;font-size:13px;color:#666;padding:14px 15px}
.btn-send{left:348px;top:3779px;width:199px;height:46px;background:var(--red);color:var(--white)}
.info{left:764px;top:3500px;width:280px;height:333px;border:1px solid var(--line);border-radius:3px}
.info-item{position:absolute;left:0;width:280px;text-align:center;font-size:13px;color:#666;line-height:24px}
.info-sep{position:absolute;left:43px;width:194px;height:1px;background:var(--line)}

/* footer */
.foot-nav a{position:absolute;top:3891px;font-size:13px;color:#777;text-decoration:none}
.foot-nav a.active{color:var(--red)}
.foot-line{left:0;top:3931px;width:1200px;height:1px;background:#ececec}
.copy{left:0;width:1200px;top:3952px;text-align:center;font-size:12px;color:#777}
</style>
</head>
<body>

<!-- Hero -->
<section class="abs hero">
  <div class="abs" role="img" aria-label="Photo of a businessman in a suit seated in a purple lounge chair checking his phone in a modern office" style="left:0;top:0;width:1200px;height:640px;background:radial-gradient(ellipse at 75% 40%,rgba(74,52,140,.55),transparent 45%),radial-gradient(ellipse at 15% 60%,rgba(74,52,140,.5),transparent 40%)"></div>
  <nav class="abs nav">
    <span class="brand">Tallo</span>
    <a style="left:508px">Home</a>
    <a style="left:590px">About Me</a>
    <a style="left:696px">Intro</a>
    <a style="left:769px">Tallo App</a>
    <a style="left:871px">Case Studies</a>
    <a style="left:999px">Contact</a>
  </nav>
  <h1 class="abs hero-title"><b>Tallo combines</b> hands-on financial planning services with real-time mobile monitoring.</h1>
  <span class="btn btn-hero notch">Let's Talk</span>
  <svg class="abs" style="left:0;top:530px" width="1200" height="111" viewBox="0 0 1200 111"><path d="M440 111 C500 111 520 15 600 15 C680 15 700 111 760 111 Z" fill="#fff"/></svg>
</section>

<!-- About -->
<h2 class="abs about-title">About Us</h2>
<div class="abs about-text">
  <p><span class="hl-purple">Small businesses</span> can visualize their finances, have a plan they trust and monitor progress daily. No more waiting for the latest monthly or quarterly report from your accountant. No more late nights digging through spreadsheets to figure out where you really stand. No more wondering if you're prepared for the future.</p>
  <p>Tallo delivers a clear financial plan tailored to your goals, an easy mobile dashboard to track progress on a daily basis and all the professional advice and support you need along the way.</p>
</div>
<span class="btn btn-about notch">Discover More</span>
<div class="abs" role="img" aria-label="Black and white photo of a man in a suit and sunglasses sitting and reading a tablet" style="left:688px;top:719px;width:352px;height:480px;background:linear-gradient(135deg,#d8d8d8,#9a9a9a 55%,#3a3a3a)"></div>
<div class="abs exp-card">
  <div class="exp-num">14</div>
  <div class="exp-label">Years of <span class="hl-purple">Experience</span></div>
</div>

<!-- How it works -->
<svg class="abs" style="left:0;top:1281px" width="1200" height="859" viewBox="0 0 1200 859">
  <path d="M0 0 H680 C760 0 790 93 862 93 C934 93 960 0 1030 0 H1200 V859 H0 Z" fill="var(--teal)"/>
  <g fill="#fff" stroke="#fff">
    <polygon points="297,163 445,248.5 445,419.5 297,505 149,419.5 149,248.5" fill="none" stroke-width="1.5"/>
    <polygon points="297,174 436,254 436,414 297,494 158,414 158,254" stroke="none"/>
    <polygon points="601,163 749,248.5 749,419.5 601,505 453,419.5 453,248.5" fill="none" stroke-width="1.5"/>
    <polygon points="601,174 740,254 740,414 601,494 462,414 462,254" stroke="none"/>
    <polygon points="905,163 1053,248.5 1053,419.5 905,505 757,419.5 757,248.5" fill="none" stroke-width="1.5"/>
    <polygon points="905,174 1044,254 1044,414 905,494 766,414 766,254" stroke="none"/>
    <polygon points="449,427 597,512.5 597,683.5 449,769 301,683.5 301,512.5" fill="none" stroke-width="1.5"/>
    <polygon points="449,438 588,518 588,678 449,758 310,678 310,518" stroke="none"/>
    <polygon points="753,427 901,512.5 901,683.5 753,769 605,683.5 605,512.5" fill="none" stroke-width="1.5"/>
    <polygon points="753,438 892,518 892,678 753,758 614,678 614,518" stroke="none"/>
  </g>
  <g fill="var(--teal)">
    <polygon points="297,228 333,249 333,291 297,312 261,291 261,249"/>
    <polygon points="601,228 637,249 637,291 601,312 565,291 565,249"/>
    <polygon points="905,228 941,249 941,291 905,312 869,291 869,249"/>
    <polygon points="449,490 485,511 485,553 449,574 413,553 413,511"/>
    <polygon points="753,490 789,511 789,553 753,574 717,553 717,511"/>
  </g>
  <g fill="none" stroke="#fff" stroke-width="1.8" stroke-linecap="round" stroke-linejoin="round">
    <rect x="281" y="255" width="26" height="30" rx="2"/><circle cx="291" cy="266" r="6"/><path d="M291 260v6h6"/>
    <path d="M301 285v-10M306 285v-14M311 285v-7"/>
    <path d="M589 257h18l6 6v22h-24z"/><path d="M593 265h12M593 271h14M593 277h10"/>
    <rect x="896" y="253" width="18" height="33" rx="3"/><path d="M903 257h4M905 282h0"/>
    <path d="M433 532c8-10 24-10 32 0c-8 10-24 10-32 0z"/><circle cx="449" cy="532" r="4.5"/>
    <circle cx="753" cy="523" r="8"/><path d="M740 548c2-9 8-13 13-13s11 4 13 13z"/><path d="M744 523c0-7 4-11 9-11s9 4 9 11"/>
  </g>
</svg>
<h2 class="abs how-title">How it Works</h2>
<div class="step" style="left:182px;top:1611px"><span class="num" style="left:18px;top:-72px">1</span><h3>Develop Plan</h3><p>We work with you to develop a<br>3 to 5 year financial plan tai-<br>lored to your business goals.</p></div>
<div class="step" style="left:486px;top:1611px"><span class="num" style="left:16px;top:-72px">2</span><h3>Clean Data</h3><p>Our bookkeepers clean your<br>historical data, set-up live data<br>intake, and ensure alignment<br>with finance reports.</p></div>
<div class="step" style="left:790px;top:1611px"><span class="num" style="left:20px;top:-72px">3</span><h3>Visual Finances</h3><p>We launch your customized<br>visual finance dashboard on<br>Tallo Mobile.</p></div>
<div class="step" style="left:334px;top:1874px"><span class="num" style="left:18px;top:-72px">4</span><h3>Monitor Daily</h3><p>You monitor real financial re-<br>sults against plan on a daily<br>basis</p></div>
<div class="step" style="left:638px;top:1874px"><span class="num" style="left:18px;top:-72px">5</span><h3>Advise Monthly</h3><p>Our financial experts provide<br>support and help respond as<br>your business grows</p></div>

<!-- Visual finance -->
<h2 class="abs vf-title">Visual Finance</h2>
<div class="abs" role="img" aria-label="Two smartphones showing the goals list and global sales dashboard of the mobile app" style="left:155px;top:2298px;width:306px;height:404px">
  <div class="abs" style="left:0;top:0;width:185px;height:400px;border:3px solid #c9ccd2;border-radius:26px;background:linear-gradient(180deg,#f4f6f8 0%,#f4f6f8 18%,#eef1f4 100%)"></div>
  <div class="abs" style="left:135px;top:50px;width:171px;height:354px;border:3px solid #c9ccd2;border-radius:24px;background:#fff"></div>
  <div class="abs" style="left:147px;top:100px;width:147px;height:258px;background:linear-gradient(180deg,#1d2f6b,#2b4a9a)"></div>
</div>
<div class="abs vf-text">
  <p><span class="hl-teal">&raquo;&nbsp; Small businesses</span> shouldn't be forced to choose between the strategic value of traditional financial services and the convenience of modern mobile reporting technology.</p>
  <p><span class="hl-teal">&raquo;&nbsp; With Tallo</span>, you have access to decades of financial planning experience and a daily view into real finance reports - all delivered through a mobile app you can take with you on the road,in the field, on the shop floor or wherever you need to be.</p>
</div>
<span class="btn btn-vf notch">Read More</span>

<!-- Why -->
<svg class="abs" style="left:0;top:2819px" width="1200" height="520" viewBox="0 0 1200 520">
  <path d="M0 0 H420 C500 0 530 93 600 93 C670 93 700 0 780 0 H1200 V520 H0 Z" fill="var(--red)"/>
</svg>
<div class="abs" role="img" aria-label="Tilted smartphones showing finance dashboards along the left edge" style="left:-60px;top:2880px;width:190px;height:360px;transform:rotate(30deg);border-radius:24px;background:linear-gradient(180deg,rgba(255,220,225,.85),rgba(200,170,210,.8))"></div>
<div class="abs" role="img" aria-label="Tilted smartphones showing finance dashboards along the right edge" style="left:1040px;top:2920px;width:180px;height:340px;transform:rotate(-35deg);border-radius:24px;background:linear-gradient(180deg,rgba(255,220,225,.85),rgba(150,140,200,.8))"></div>
<h2 class="abs why-title">Why Tallo Visual Finance?</h2>
<div class="abs why-text">
  <p><b>Small businesses</b> shouldn't be forced to choose between the strategic value of traditional financial services and the convenience of modern mobile reporting technology.</p>
  <p>With Tallo, you have access to decades of <b>financial planning experience</b> and a daily view into real finance reports - all delivered through a mobile app you can take with you on the road, in the field, on the shop floor or wherever you need to be.</p>
</div>
<span class="btn btn-why notch">Read More</span>

<!-- Contact -->
<h2 class="abs contact-title">Contact Us</h2>
<div class="field" style="top:3500px;height:47px">Name</div>
<div class="field" style="top:3564px;height:47px">Email</div>
<div class="field" style="top:3629px;height:117px">Your Message</div>
<span class="btn btn-send notch">Send Message</span>
<div class="abs info">
  <svg class="abs" style="left:133px;top:44px" width="14" height="14" viewBox="0 0 24 24"><path d="M6.6 10.8c1.4 2.8 3.8 5.1 6.6 6.6l2.2-2.2c.3-.3.7-.4 1-.2 1.1.4 2.3.6 3.6.6.6 0 1 .4 1 1V20c0 .6-.4 1-1 1C10.6 21 3 13.4 3 4c0-.6.4-1 1-1h3.5c.6 0 1 .4 1 1 0 1.3.2 2.5.6 3.6.1.3 0 .7-.2 1z" fill="var(--red)"/></svg>
  <div class="info-item" style="top:64px">Phone Number<br>+1 555 014 3390</div>
  <div class="info-sep" style="top:130px"></div>
  <svg class="abs" style="left:133px;top:144px" width="14" height="11" viewBox="0 0 14 11"><rect width="14" height="11" rx="1.5" fill="var(--red)"/><path d="M1 1.5l6 4.5 6-4.5" stroke="#fff" stroke-width="1.2" fill="none"/></svg>
  <div class="info-item" style="top:160px">Email Address<br>info@example.com</div>
  <div class="info-sep" style="top:226px"></div>
  <svg class="abs" style="left:134px;top:238px" width="12" height="16" viewBox="0 0 12 16"><path d="M6 0C2.7 0 0 2.6 0 5.9 0 10.3 6 16 6 16s6-5.7 6-10.1C12 2.6 9.3 0 6 0z" fill="var(--red)"/><circle cx="6" cy="6" r="2.2" fill="#fff"/></svg>
  <div class="info-item" style="top:256px">Email Address<br>info@example.com</div>
</div>

<!-- Footer -->
<nav class="foot-nav">
  <a class="active" style="left:297px">Home</a>
  <a style="left:391px">About Me</a>
  <a style="left:513px">Intro</a>
  <a style="left:596px">Tallo App</a>
  <a style="left:712px">Case Studies</a>
  <a style="left:851px">Contact</a>
</nav>
<div class="abs foot-line"></div>
<div class="abs copy">© 2019 by Tallo Consulting</div>

</body>
</html>
```